Audio Visual company needs brochure design

We are an AV company that does Audio Visual work solely for Commercial customers. We Design, sale and install various Audio Visual systems for our customers. This may be something as simple as a conference room, a new sound system for a church or a new sound, lighting and video system for an arena or stadium.

We don't really have any ideas in mind and that's the reason we are turning to you. We want something that highlights what we do, and something they will look at - not just toss in the can.

Included is a copy of our logo (sorry it's the only copy we have now)

Our company name is Velmira Staging www.velmirastaging.example
Updates

Reason: The rest of our management team hasn't provided feedback to me yet. We will pick the design this week.

Target Market(s)

70% of our business is churches and the remaining is corporate customers and restaurants.

Industry/Entity Type

Church

Requirements
Must have
• The brochure will be 8.5" x 11" printed both sides - open to Z fold or Tri fold designs. We can provide pictures of our work if needed - though they may not be the best.
Should not have
• No generic pictures of just speakers, projectors, microphones, etc.

```html
<!DOCTYPE html>
<html lang="en">
<head>
<meta charset="utf-8">
<title>Velmira Staging – Brochure Inside Spread</title>
<link href="https://fonts.googleapis.com/css2?family=Roboto:wght@300&family=Italianno&family=Oswald:wght@600&display=swap" rel="stylesheet">
<style>
  :root {
    --bg: #231f20;
    --text: #f2f2f2;
    --accent: #e8262b;
    --haze-1: #7fc3d6;
    --haze-2: #2f5f8a;
    --haze-3: #3a2f55;
  }
  * { margin: 0; padding: 0; box-sizing: border-box; }
  html, body { width: 1200px; height: 928px; overflow: hidden; background: var(--bg); }
  .spread {
    position: relative;
    width: 1200px;
    height: 928px;
    background: var(--bg);
    font-family: 'Roboto', Helvetica, Arial, sans-serif;
    font-weight: 300;
    color: var(--text);
    overflow: hidden;
  }
  .hero-photo {
    position: absolute;
    left: 0; top: 0;
    width: 760px; height: 620px;
    background:
      radial-gradient(ellipse 160px 260px at 150px 230px, rgba(200,230,240,0.55), transparent 70%),
      radial-gradient(ellipse 260px 220px at 420px 120px, rgba(127,195,214,0.55), transparent 75%),
      radial-gradient(ellipse 220px 200px at 230px 330px, rgba(47,95,138,0.7), transparent 75%),
      radial-gradient(ellipse 200px 160px at 560px 300px, rgba(58,47,85,0.5), transparent 75%),
      radial-gradient(ellipse 380px 320px at 300px 260px, rgba(30,60,80,0.6), transparent 80%);
  }
  .column { position: absolute; width: 265px; }
  .column--services { left: 68px; top: 418px; }
  .column--installations { left: 468px; top: 56px; width: 262px; }
  .column--rentals { left: 869px; top: 56px; width: 270px; }
  .section-title {
    font-family: 'Italianno', cursive;
    font-weight: 400;
    font-size: 58px;
    line-height: 1;
    color: var(--text);
    margin-bottom: -2px;
  }
  .column--services .section-title { font-size: 46px; }
  .block { margin-bottom: 16px; }
  .block h3 {
    font-weight: 300;
    font-size: 14.5px;
    line-height: 15px;
    color: var(--accent);
    text-transform: uppercase;
  }
  .block p {
    font-size: 13.6px;
    line-height: 15.2px;
  }
  .tagline {
    position: absolute;
    left: 468px; top: 830px;
    font-family: 'Oswald', 'Arial Narrow', sans-serif;
    font-weight: 600;
    font-size: 16px;
    line-height: 19px;
    color: var(--accent);
    letter-spacing: -0.2px;
  }
</style>
</head>
<body>
<div class="spread">
  <div class="hero-photo" role="img" aria-label="Vintage stage microphone under blue concert lights with a raised hand in the crowd"></div>

  <div class="column column--services">
    <h2 class="section-title">services</h2>
    <div class="block">
      <h3>Event Production</h3>
      <p>Velmira Staging has been a leader in the production industry. We are a full scale touring production company that owns and maintains an impressive inventory of the latest technology in audio, video, lighting and staging equipment. Velmira Staging can substantially cut your costs by being a one stop shop.</p>
    </div>
    <div class="block">
      <h3>Repairs</h3>
      <p>The Velmira Staging service department is second to none. Our service techs are responsible handles service calls and offers bench repair for most of the Pro audio, lighting &amp; video manufactures.</p>
    </div>
    <div class="block">
      <h3>Custom Fabrication</h3>
      <p>Velmira Staging has an in-house fabrication shop that supports our role as a full service AV and Production Company. Our fabrication shop is staffed by experienced carptners who have over 15 years experience.</p>
    </div>
  </div>

  <div class="column column--installations">
    <h2 class="section-title">instalations</h2>
    <div class="block">
      <h3>Churches</h3>
      <p>As churches become larger and more advance with their teachings, so does the equipment requried to deliver that important message. Our engineers and technicians have experience in worship A/V not only because that is one of the largest shares of our business but because we are active in our own churches running the equipment.</p>
    </div>
    <div class="block">
      <h3>Corporate</h3>
      <p>We have worked with many corporate clients updating and intergrating new technology. From background music in a food chain to class rooms and board rooms, we've done it all. Working with you from the begining, our designers and project engineers ensure everything is in place during the critical times of construction. From rough-in to punch out, we are there every step of the way saving you valuable time and money.</p>
    </div>
    <div class="block">
      <h3>Entertainment</h3>
      <p>Velmira Staging has been called on time and time again to design, install and fix Sound, Lighting and Video systems in many of the areas entertainment establishments. Our expertise have made us the favorite and in-house provider for many places.</p>
    </div>
    <div class="block">
      <h3>The Process</h3>
      <p>System intergration is not like it was once upon a time. AV systems have become sophisticated and peoples standards have grown dramatically. In the old days one would simply hang a speaker and aim it by what looked right with no thought of the room, it's contents and the people in mind.</p>
    </div>
  </div>

  <div class="column column--rentals">
    <h2 class="section-title">rentals</h2>
    <div class="block">
      <h3>Sound</h3>
      <p>We have all the gear you need to be heard and the staff to run it! We carry all the big names including Corvane, Thalric, Brennan &amp; Voss, Orlith, Sonavex, Kestrow, Halden, Marrowfield, Quillon, Vantrel, Ebrin and Pelmor to name just a few. It doesn't matter if it's a crowd of 20 or 20,000-We have the gear requried to handle your event indoors and out!</p>
    </div>
    <div class="block">
      <h3>Lighting</h3>
      <p>We provide accent lighting for Weddings, Corporate and Tradeshow events and theatrical lighting for shows.</p>
    </div>
    <div class="block">
      <h3>Video</h3>
      <p>We offer Projectors, Plasmas, LCD monitors, Screens, video switchers and media servers. For more information on the gear we stock.</p>
    </div>
    <div class="block">
      <h3>Staging</h3>
      <p>We offers a large selection of Staging and Trussing. Velmira Staging uses Rostavel and Deckline Stages stages, Arcwell Systems, Ferrow and Latticeon truss and Hoistra motors.</p>
    </div>
    <div class="block">
      <h3>Misc.</h3>
      <p>We offers everything you need to support your show. Power distros for FOH &amp; Lighting, Cable ramps to cover the cabling, Bicycle rack barricades, Intercom and Two-way radios.</p>
    </div>
    <div class="block">
      <h3>Wedding</h3>
      <p>We offer everything from a simple powered speaker with a wireless mic for your officiant to use at your ceremony to lighting packages used to transform your reception into something never seen!</p>
    </div>
  </div>

  <p class="tagline">We specialize in all aspects of sound reinforcement, lighting, video and staging systems<br>in both the installation and production markets.</p>
</div>
</body>
</html>
```